New business card design needed for Trucking/Staffing company!

I am looking for a business card design. The business name is Harbor Lane Freightworks, LLC. This company is a staffing company for commercial drivers/truck drivers. Most of our customers are trucking/supply companies. Our colors are blue/black/white/grey. The info I have on my current business cards is
-Spot for a name
-2 lines for an address
-3 lines for Office, cell, and fax
-email
-website(currently on backside of card with logo but can go anywhere)
Updates

Project Deadline Extended
Reason: Open to more designs

Target Market(s)

Trucking companies, building supply companies

Industry/Entity Type

Business

Contact Information for Business Card

Edgy but professional

Font styles to use
Other font styles liked:
• Open to suggestions

Colors
0555a3
000000
ffffff
9d9d9d

Requirements
Must have
• Must have the logo incorporated

```html
<!DOCTYPE html>
<html lang="en">
<head>
<meta charset="utf-8">
<title>Harbor Lane Freightworks – Business Card</title>
<link rel="stylesheet" href="https://fonts.googleapis.com/css2?family=Lato:wght@400;700&display=swap">
<style>
  :root {
    --brand-blue: #2f3a9e;
    --ink-black: #111111;
    --card-black: #1c1c1c;
    --paper-white: #ffffff;
    --rule-grey: #9d9d9d;
    --text-grey: #3a3a3a;
    --stage: #e9e7e3;
  }
  * { box-sizing: border-box; margin: 0; padding: 0; }
  html, body { width: 1200px; height: 1023px; overflow: hidden; }
  body {
    background: var(--stage);
    font-family: "Lato", Arial, sans-serif;
    position: relative;
  }
  .card {
    position: absolute;
    width: 640px;
    height: 366px;
    border-radius: 14px;
    overflow: hidden;
    box-shadow: 0 8px 24px rgba(0,0,0,0.18);
  }
  /* Front */
  .card-front {
    left: 60px; top: 70px;
    background: linear-gradient(160deg, var(--paper-white) 40%, #ececec 100%);
  }
  .card-front .accent-band {
    position: absolute; left: 0; right: 0; bottom: 0; height: 12px;
    background: var(--brand-blue);
  }
  .wordmark {
    display: flex; align-items: center; gap: 12px;
    font-weight: 700; letter-spacing: 0.5px;
  }
  .wordmark .mark-square {
    width: 18px; height: 18px; background: currentColor;
  }
  .card-front .wordmark {
    position: absolute; left: 150px; top: 56px;
    color: var(--brand-blue); font-size: 30px;
  }
  .card-front .divider {
    position: absolute; left: 170px; right: 40px; top: 134px;
    height: 1px; background: var(--text-grey);
  }
  .contact-block { position: absolute; left: 44px; top: 190px; }
  .person-name { color: var(--brand-blue); font-weight: 700; font-size: 22px; }
  .person-title { color: var(--text-grey); font-size: 16px; margin-top: 2px; }
  .name-rule { width: 150px; height: 1px; background: var(--text-grey); margin: 6px 0 12px; }
  .contact-list { list-style: none; font-size: 16px; color: var(--text-grey); line-height: 22px; }
  .contact-list li { display: flex; align-items: center; gap: 9px; }
  .contact-list svg { width: 13px; height: 13px; fill: var(--brand-blue); flex: none; }
  .address-block {
    position: absolute; right: 44px; top: 154px;
    text-align: right; font-size: 17px; color: var(--text-grey); line-height: 23px;
  }
  /* Back */
  .card-back {
    left: 500px; top: 560px;
    background: radial-gradient(ellipse at 35% 30%, #3a3a3a 0%, var(--card-black) 60%, var(--ink-black) 100%);
  }
  .card-back .wordmark {
    position: absolute; left: 0; right: 0; top: 130px; justify-content: center;
    color: var(--brand-blue); font-size: 34px;
  }
  .card-back .site-line {
    position: absolute; left: 60px; right: 60px; top: 232px;
    display: flex; align-items: center; gap: 14px;
    color: #d8d8d8; font-size: 15px; font-style: italic;
  }
  .card-back .site-line::before,
  .card-back .site-line::after {
    content: ""; flex: 1; height: 1px; background: var(--rule-grey);
  }
</style>
</head>
<body>

<section class="card card-front" aria-label="Business card front">
  <div class="wordmark"><span class="mark-square"></span>Harbor Lane Freightworks</div>
  <div class="divider"></div>

  <div class="contact-block">
    <p class="person-name">Dana Whitfield</p>
    <p class="person-title">President</p>
    <div class="name-rule"></div>
    <ul class="contact-list">
      <li><svg viewBox="0 0 12 12"><rect x="3" y="0" width="6" height="12" rx="1"/></svg>01357924680</li>
      <li><svg viewBox="0 0 12 12"><path d="M2 1h3l1 3-2 1a7 7 0 0 0 3 3l1-2 3 1v3a1 1 0 0 1-1 1A10 10 0 0 1 1 2a1 1 0 0 1 1-1z"/></svg>+0864213579</li>
      <li><svg viewBox="0 0 12 12"><rect x="3" y="0" width="6" height="4"/><rect x="0" y="4" width="12" height="5"/><rect x="3" y="8" width="6" height="4"/></svg>+0864213579</li>
      <li><svg viewBox="0 0 12 12"><path d="M0 2h12v8H0z M1 3l5 4 5-4" stroke="#fff" stroke-width="1"/></svg>info@harborlanefreight.com</li>
    </ul>
  </div>

  <div class="address-block">
    <p>Your Business address</p>
    <p>Harbor Lane Freightworks, LLC</p>
  </div>

  <div class="accent-band"></div>
</section>

<section class="card card-back" aria-label="Business card back">
  <div class="wordmark"><span class="mark-square"></span>Harbor Lane Freightworks</div>
  <p class="site-line">www.harborlanefreight.com</p>
</section>

</body>
</html>
```